VELOMIRA needs a label design for their product line of therapeutic CBD HEMP oil.

We are a company based out of Hawaii, USA called "VeloMira". We are needing a new look for our labels on our 2 oz bottles of CBD hemp oil. We are using organic CBD rich hemp oil and combining it with other organic oils to help heal inflammation, skin problems, and other ailments.

We have 6 different products of CBD oils :
x 2 CBD oil tinctures ( internal) : ZENITH CBD and BOTANIQ FORMULA
x 3 CBD skin care oils (external): CBD FACIAL SOLSTICE, CBD BODY
OIL, and CBD SKIN CARE
x 1 CBD Therapeutic oil ( external) SOOTHAVEX - Inflammation
Each product is in a 2 oz amber bottle with a black mist sprayer cap or black dropper and is a different color label. A green bottle ( zenith cbd), blue (botaniq), yellow(body oil), red/pink (restorative), purple( soothavex) the other colors???
I would like to use the color gold in our labels.

There is the logo for the name 'VeloMira", an oil droplet, and hemp leaf on each bottle.
I have the descriptive text/layout for the wording to be placed on the side of the bottles which just need a little font finessing.
I have designed the labels but just cannot seem to make them look professional and would like to re create the look.

I am seeking a label that looks professional for a successful business of high quality oils.

Target Market(s)

health food stores, alternative medicines, internet,

Industry/Entity Type

Graphic Design

Requirements
Must have
• I would like the word or logo for organic on the bottle.
• There must be a small space left for the bar code.
• I would like them all to look similar just with different colors and a slight different layout to distinguish the 2 internal CBD tiinctures ( CBD ZENTIH, BOTANIQ FORMULA) + soothavex from the 3 skin care external skin oils.
Nice to have
• I would like my product to have a hemp leaf somewhere on it but not too obvious.
• I am more concerned with the front design of the bottles than the written words on the sides of the bottle. That could be worked on later.
Should not have
• my label should not look too busy!

```html
<!DOCTYPE html>
<html lang="en">
<head>
<meta charset="utf-8">
<title>VeloMira Label Line</title>
<link rel="stylesheet" href="https://fonts.googleapis.com/css2?family=Didact+Gothic&family=Roboto+Condensed:wght@700&display=swap">
<style>
  :root {
    --page: #eef3ec;
    --ink: #3a3a3a;
    --ink-soft: #6a6a6a;
    --white: #ffffff;
    --purple: #8d3f98;
    --purple-light: #d6b3dc;
    --purple-deep: #5f2468;
    --yellow: #e7b51f;
    --yellow-light: #f6e29a;
    --yellow-deep: #a87f0c;
    --teal: #4bb0a5;
    --teal-light: #b5e0da;
    --teal-deep: #2c7a72;
    --blue: #2a7dbf;
    --blue-light: #b4d4ee;
    --blue-deep: #1b5689;
  }
  * { box-sizing: border-box; margin: 0; padding: 0; }
  html, body { width: 1200px; height: 694px; overflow: hidden; }
  body {
    background: var(--page);
    font-family: "Didact Gothic", sans-serif;
    color: var(--ink);
  }
  .label-line {
    position: relative;
    width: 1200px;
    height: 694px;
  }
  .label {
    position: absolute;
    top: 172px;
    width: 200px;
    height: 350px;
    background: var(--white);
    border-radius: 4px;
    overflow: hidden;
    box-shadow: 0 4px 14px rgba(0,0,0,0.12);
    text-align: center;
  }
  .label--soothavex { left: 158px; --tone: var(--purple); --tone-light: var(--purple-light); --tone-deep: var(--purple-deep); }
  .label--restorative { left: 377px; --tone: var(--yellow); --tone-light: var(--yellow-light); --tone-deep: var(--yellow-deep); }
  .label--zenith { left: 613px; --tone: var(--teal); --tone-light: var(--teal-light); --tone-deep: var(--teal-deep); }
  .label--botaniq { left: 848px; --tone: var(--blue); --tone-light: var(--blue-light); --tone-deep: var(--blue-deep); }

  .label__texture {
    position: absolute;
    left: 0; top: 0;
    width: 100%; height: 62px;
  }
  .label__texture-fill { fill: var(--tone-light); }
  .label__wave { fill: var(--white); }
  .label__base {
    position: absolute;
    left: 0; bottom: 0;
    width: 100%; height: 12px;
    background: linear-gradient(90deg, var(--tone-light), var(--tone), var(--tone-light));
    opacity: 0.75;
  }
  .brand {
    position: absolute;
    top: 82px; left: 0; width: 100%;
    font-size: 27px;
    color: var(--ink);
    letter-spacing: 0.2px;
  }
  .banner {
    position: absolute;
    top: 136px; left: 6px;
    width: 188px; height: 36px;
    background: linear-gradient(180deg, var(--tone), var(--tone-deep) 140%);
    color: var(--white);
    font-family: "Roboto Condensed", sans-serif;
    font-weight: 700;
    font-size: 18px;
    line-height: 36px;
    letter-spacing: 0.8px;
  }
  .banner::before, .banner::after {
    content: "";
    position: absolute;
    top: 36px;
    border-top: 6px solid var(--tone-deep);
  }
  .banner::before { left: 0; border-left: 6px solid transparent; }
  .banner::after { right: 0; border-right: 6px solid transparent; }
  .details {
    position: absolute;
    top: 184px; left: 0; width: 100%;
    padding: 0 14px;
  }
  .details__subtitle {
    font-size: 12.5px;
    letter-spacing: 1px;
    text-transform: uppercase;
    color: var(--ink);
  }
  .details__line {
    font-size: 12.5px;
    line-height: 1.35;
    color: var(--ink);
  }
  .details__accent {
    margin-top: 10px;
    font-size: 11.5px;
    line-height: 1.35;
    color: var(--tone);
  }
  .details__accent--caps {
    text-transform: uppercase;
    font-size: 9.5px;
    letter-spacing: 0.3px;
    color: var(--tone-deep);
  }
  .details__volume {
    position: absolute;
    top: 312px; left: 0; width: 100%;
    font-size: 9px;
    color: var(--ink-soft);
  }
  .label--soothavex .details__accent { margin-top: 14px; font-size: 12px; }
</style>
</head>
<body>
<main class="label-line">

  <section class="label label--soothavex">
    <svg class="label__texture" viewBox="0 0 200 62" preserveAspectRatio="none" role="img" aria-label="Shimmering purple texture band">
      <rect class="label__texture-fill" width="200" height="62"/>
      <path class="label__wave" d="M0 40 Q100 26 200 40 L200 62 L0 62 Z"/>
    </svg>
    <div class="brand">VeloMira</div>
    <div class="banner">SOOTHAVEX</div>
    <div class="details">
      <p class="details__line">CBD Rich Hemp Oil &amp;</p>
      <p class="details__line">BCP Rich Copaiba Oil</p>
      <p class="details__accent">Pure, Natural Organic Oils</p>
    </div>
    <p class="details__volume">2 Fl Oz. / 60ml</p>
    <div class="label__base"></div>
  </section>

  <section class="label label--restorative">
    <svg class="label__texture" viewBox="0 0 200 62" preserveAspectRatio="none" role="img" aria-label="Shimmering golden texture band">
      <rect class="label__texture-fill" width="200" height="62"/>
      <path class="label__wave" d="M0 40 Q100 26 200 40 L200 62 L0 62 Z"/>
    </svg>
    <div class="brand">VeloMira</div>
    <div class="banner">RESTORATIVE</div>
    <div class="details">
      <p class="details__subtitle">Treatment Oil</p>
      <p class="details__accent details__accent--caps">With Hemp CBD Oil<br>&amp; Cucumber Oil</p>
    </div>
    <p class="details__volume">4 Fl Oz. / 180ml</p>
    <div class="label__base"></div>
  </section>

  <section class="label label--zenith">
    <svg class="label__texture" viewBox="0 0 200 62" preserveAspectRatio="none" role="img" aria-label="Shimmering teal texture band">
      <rect class="label__texture-fill" width="200" height="62"/>
      <path class="label__wave" d="M0 40 Q100 26 200 40 L200 62 L0 62 Z"/>
    </svg>
    <div class="brand">VeloMira</div>
    <div class="banner">CBD ZENITH</div>
    <div class="details">
      <p class="details__line">CBD Rich Hemp Oil</p>
      <p class="details__line">Organic CO2 Extract</p>
      <p class="details__accent">500mg Cannabidiol</p>
    </div>
    <p class="details__volume">1 Fl Oz. / 30ml Dietary Supplement</p>
    <div class="label__base"></div>
  </section>

  <section class="label label--botaniq">
    <svg class="label__texture" viewBox="0 0 200 62" preserveAspectRatio="none" role="img" aria-label="Shimmering blue texture band">
      <rect class="label__texture-fill" width="200" height="62"/>
      <path class="label__wave" d="M0 40 Q100 26 200 40 L200 62 L0 62 Z"/>
    </svg>
    <div class="brand">VeloMira</div>
    <div class="banner">BOTANIQ</div>
    <div class="details">
      <p class="details__subtitle">Formula</p>
      <p class="details__accent">500mg Cannabidiol<br>150mg &beta; - Caryophyllene</p>
    </div>
    <p class="details__volume">1 Fl Oz. / 30ml Dietary Supplement</p>
    <div class="label__base"></div>
  </section>

</main>
</body>
</html>
```